Clark County Assessor Canditate

We need a billboard ad for a political candidate Tessa Harrow who is running for Clark County Assessor in an upcoming election. Needs to be simple and to the point to get the people to see the name "Tessa Harrow" and what to vote for "Clark County Assessor" in Las Vegas, NV. Also the billboard visibility is best in the top side of the sign, so the information should be most prominent in the top right, middle, left sides.The size of the billboard is 14 ft Height X 48 ft Wide Also needs some bright colors that are noticable from a freeway viewed billboard.Designers - I need to have "Paid for by Tessa Harrow for Clark County Assessor" on the sign
I have uploaded a few headshots you can work with to create a design. Thank you,

http://tessaharrow-vote.info/

Voters

Political

• Name, what I am voting for, and some image that represents Las Vegas and/or Nevada

```html
<!DOCTYPE html>
<html lang="en">
<head>
<meta charset="utf-8">
<title>Tessa Harrow – Clark County Assessor Billboard</title>
<link rel="stylesheet" href="https://fonts.googleapis.com/css2?family=Source+Sans+3:ital,wght@0,400;0,600;0,700;1,600&display=swap">
<style>
  :root {
    --backdrop: #e9edf2;
    --board-white: #ffffff;
    --campaign-blue: #2a4b9f;
    --campaign-orange: #f08a22;
    --skyline-dusk: #7c8fae;
    --skyline-warm: #c9a88a;
    --skyline-deep: #4a5a78;
  }
  * { margin: 0; padding: 0; box-sizing: border-box; }
  html, body {
    width: 1200px;
    height: 598px;
    overflow: hidden;
    background: var(--backdrop);
    font-family: "Source Sans 3", "Helvetica Neue", Arial, sans-serif;
  }
  .billboard {
    position: absolute;
    left: 20px;
    top: 130px;
    width: 1160px;
    height: 338px;
    background: var(--board-white);
    overflow: hidden;
  }
  .top-band {
    position: absolute;
    left: 0; top: 0;
    width: 100%;
    height: 13px;
    background: var(--campaign-blue);
  }
  .candidate-photo {
    position: absolute;
    left: 0;
    top: 13px;
    width: 480px;
    height: 242px;
    background:
      linear-gradient(to right, rgba(255,255,255,0) 0%, rgba(255,255,255,0) 62%, var(--board-white) 100%),
      linear-gradient(to bottom, var(--skyline-dusk) 0%, var(--skyline-warm) 55%, var(--skyline-deep) 100%);
  }
  .message {
    position: absolute;
    left: 481px;
    top: 0;
    right: 55px;
    height: 255px;
  }
  .slogan {
    position: absolute;
    left: 0;
    top: 34px;
    font-size: 44px;
    font-weight: 600;
    font-style: italic;
    color: var(--campaign-orange);
    line-height: 1;
  }
  .candidate-name {
    position: absolute;
    left: -4px;
    top: 76px;
    font-size: 92px;
    font-weight: 600;
    color: var(--campaign-orange);
    line-height: 1;
    letter-spacing: -0.5px;
    white-space: nowrap;
  }
  .office {
    position: absolute;
    right: 0;
    top: 192px;
    font-size: 40px;
    font-weight: 600;
    color: var(--campaign-blue);
    line-height: 1;
    letter-spacing: -0.3px;
  }
  .disclaimer {
    position: absolute;
    left: 0;
    top: 238px;
    font-size: 12px;
    font-weight: 400;
    color: var(--campaign-blue);
    line-height: 1;
    white-space: nowrap;
  }
  .location-band {
    position: absolute;
    left: 0;
    bottom: 0;
    width: 100%;
    height: 83px;
    background: var(--campaign-blue);
  }
  .location {
    position: absolute;
    right: 52px;
    top: 50%;
    transform: translateY(-50%);
    font-size: 31px;
    font-weight: 600;
    color: var(--board-white);
    letter-spacing: 10px;
    line-height: 1;
    white-space: nowrap;
  }
</style>
</head>
<body>
  <div class="billboard">
    <div class="top-band"></div>
    <div class="candidate-photo" role="img" aria-label="Headshot of candidate Tessa Harrow in front of the Las Vegas Strip skyline"></div>
    <div class="message">
      <p class="slogan">“Working for You”</p>
      <h1 class="candidate-name">Tessa Harrow</h1>
      <p class="office">Clark County Assessor</p>
      <p class="disclaimer">Paid for by Tessa Harrow for Clark County Assessor</p>
    </div>
    <div class="location-band">
      <p class="location">LAS VEGAS • NEVADA</p>
    </div>
  </div>
</body>
</html>
```